R&T Builders and Spaces Business Card

We need to redesign our business card. We had used white vellum wih grey logo and txt in the past. I would like to bring a little life into our cards without being over the top. I think I will be going away from the vellum and printing soft touch business cards.
I have attached what we currently have and our new logo design.

```html
<!DOCTYPE html>
<html lang="en">
<head>
<meta charset="utf-8">
<title>R&amp;T Builders and Spaces – Business Card</title>
<link href="https://fonts.googleapis.com/css2?family=Lato:wght@400;700;900&display=swap" rel="stylesheet">
<style>
  :root {
    --page-bg: #e9e6e4;
    --card-light-1: #d9d5d5;
    --card-light-2: #efedee;
    --card-dark-1: #5e5e5e;
    --card-dark-2: #1f1f1f;
    --ink: #2a2a2a;
    --ink-soft: #3b3b3b;
    --silver: #d6d2cf;
  }
  html, body {
    margin: 0;
    width: 1200px;
    height: 734px;
    overflow: hidden;
    background: var(--page-bg);
    font-family: "Lato", sans-serif;
  }
  .business-card {
    position: absolute;
    left: 40px;
    top: 47px;
    width: 1120px;
    height: 640px;
    border-radius: 30px;
    overflow: hidden;
    box-shadow: 0 10px 30px rgba(0,0,0,0.12);
  }
  .card-shapes {
    position: absolute;
    inset: 0;
  }
  .brand {
    position: absolute;
    left: 89px;
    top: 200px;
    width: 280px;
    text-align: center;
    color: var(--silver);
  }
  .brand-square {
    width: 90px;
    height: 90px;
    margin: 0 auto 26px;
    background: var(--silver);
  }
  .brand-name {
    font-weight: 400;
    font-size: 26px;
    letter-spacing: 4px;
    line-height: 1.35;
    text-transform: uppercase;
  }
  .person {
    position: absolute;
    right: 107px;
    top: 78px;
    text-align: right;
    color: var(--ink);
  }
  .person-name {
    font-weight: 900;
    font-size: 56px;
    line-height: 1;
    letter-spacing: -0.5px;
  }
  .person-title {
    font-weight: 700;
    font-size: 29px;
    color: var(--ink-soft);
    margin-top: 8px;
    margin-right: 7px;
  }
  .contact-list {
    position: absolute;
    right: 112px;
    list-style: none;
    margin: 0;
    padding: 0;
    color: var(--ink);
    font-size: 26px;
    font-weight: 400;
  }
  .contact-list.personal { top: 216px; }
  .contact-list.office { top: 398px; }
  .contact-list li {
    height: 40px;
    line-height: 34px;
    display: flex;
    justify-content: flex-end;
    align-items: center;
  }
  .contact-list .icon {
    width: 20px;
    height: 20px;
    margin-left: 18px;
    margin-right: -38px;
    fill: var(--ink);
    flex: none;
  }
  .contact-list .no-icon { margin-right: 0; }
</style>
</head>
<body>
  <div class="business-card">
    <svg class="card-shapes" viewBox="0 0 1120 640" width="1120" height="640" aria-hidden="true">
      <defs>
        <linearGradient id="light-face" x1="0" y1="0" x2="1" y2="1">
          <stop offset="0" stop-color="var(--card-light-1)"/>
          <stop offset="1" stop-color="var(--card-light-2)"/>
        </linearGradient>
        <radialGradient id="dark-face" cx="0.25" cy="0.5" r="0.9">
          <stop offset="0" stop-color="var(--card-dark-1)"/>
          <stop offset="1" stop-color="var(--card-dark-2)"/>
        </radialGradient>
      </defs>
      <rect width="1120" height="640" fill="url(#light-face)"/>
      <polygon points="0,0 378,0 608,320 378,640 0,640" fill="url(#dark-face)"/>
      <polygon points="1011,0 1120,0 1120,152" fill="#3a3a3a"/>
      <polygon points="1120,492 1120,640 1011,640" fill="#2c2c2c"/>
    </svg>

    <div class="brand">
      <div class="brand-square"></div>
      <div class="brand-name">R&amp;T Builders<br>and Spaces</div>
    </div>

    <div class="person">
      <div class="person-name">DALE M. FORSYTHE</div>
      <div class="person-title">Principal</div>
    </div>

    <ul class="contact-list personal">
      <li>480.555.0142
        <svg class="icon" viewBox="0 0 24 24"><path d="M6.6 10.8a15.5 15.5 0 0 0 6.6 6.6l2.2-2.2c.3-.3.7-.4 1-.2 1.1.4 2.3.6 3.6.6.6 0 1 .4 1 1V20c0 .6-.4 1-1 1A17 17 0 0 1 3 4c0-.6.4-1 1-1h3.5c.6 0 1 .4 1 1 0 1.3.2 2.5.6 3.6.1.3 0 .7-.2 1z"/></svg></li>
      <li>480.555.0178
        <svg class="icon" viewBox="0 0 24 24"><path d="M7 3h10v5H7zM4 9h16a2 2 0 0 1 2 2v6h-4v4H6v-4H2v-6a2 2 0 0 1 2-2zm4 7v3h8v-3z"/></svg></li>
      <li>480 555 0193
        <svg class="icon" viewBox="0 0 24 24"><path d="M7 1h10a2 2 0 0 1 2 2v18a2 2 0 0 1-2 2H7a2 2 0 0 1-2-2V3a2 2 0 0 1 2-2zm0 3v15h10V4zm5 16.2a1 1 0 1 0 0 .1z"/></svg></li>
      <li>dalef@rtbuilders.com
        <svg class="icon" viewBox="0 0 24 24"><path d="M2 5h20v14H2zm2 2v.5l8 5 8-5V7z"/></svg></li>
    </ul>

    <ul class="contact-list office">
      <li>480.555.0100
        <svg class="icon" viewBox="0 0 24 24"><path d="M6.6 10.8a15.5 15.5 0 0 0 6.6 6.6l2.2-2.2c.3-.3.7-.4 1-.2 1.1.4 2.3.6 3.6.6.6 0 1 .4 1 1V20c0 .6-.4 1-1 1A17 17 0 0 1 3 4c0-.6.4-1 1-1h3.5c.6 0 1 .4 1 1 0 1.3.2 2.5.6 3.6.1.3 0 .7-.2 1z"/></svg></li>
      <li>www.rtbuilders.com
        <svg class="icon" viewBox="0 0 24 24"><circle cx="12" cy="12" r="10"/></svg></li>
      <li>1840 W Mesa Ridge Rd, Suite 200
        <svg class="icon" viewBox="0 0 24 24"><path d="M12 2a7 7 0 0 1 7 7c0 5-7 13-7 13S5 14 5 9a7 7 0 0 1 7-7zm0 4.5a2.5 2.5 0 1 0 0 5 2.5 2.5 0 0 0 0-5z"/></svg></li>
      <li><span class="no-icon">Tempe, Arizona 85281</span></li>
    </ul>
  </div>
</body>
</html>
```